Helix Marke Business Cards and Letterheads.
Lead Generation Specialists.
Professional
Denise Okafor
Account Manager
Wexford Court
Brindle Road
Chertsey, Surrey
RG21 4XN
UK
Denise.okafor@helixmarke.co.uk
Www.helixmarke.co.uk
In the email address please make it all lower case including the l and p in the name.
Same applies for the web address the www. Needs to all be in lower case.
We would like the background, a block colour (wash) using the blue of the text Helix Marke in our logo. We would like the logo reversed out in White together with the tag line and we would also like the inclusion of the 5 locations of our offices.
London
New York
Amsterdam
Munich
Silicon Valley

```html
<!DOCTYPE html>
<html lang="en">
<head>
<meta charset="utf-8">
<title>Helix Marke Stationery</title>
<link href="https://fonts.googleapis.com/css2?family=Open+Sans:wght@400;600&display=swap" rel="stylesheet">
<style>
  :root {
    --board: #b4b4b4;
    --paper: #ffffff;
    --brand-blue: #1f5ea8;
    --brand-orange: #f2a33a;
    --ink: #555a60;
    --ink-soft: #8a8f95;
    --wash-blue: rgba(31, 94, 168, 0.10);
    --wash-orange: rgba(242, 163, 58, 0.12);
    --fold: #d6d6d6;
  }
  * { box-sizing: border-box; margin: 0; padding: 0; }
  html, body { width: 1200px; height: 684px; overflow: hidden; }
  body {
    background: var(--board);
    font-family: "Open Sans", Arial, sans-serif;
    color: var(--ink);
    position: relative;
  }
  .sheet {
    position: absolute;
    background: var(--paper);
    box-shadow: 0 1px 3px rgba(0,0,0,0.25);
    overflow: hidden;
  }
  /* logo lockup */
  .lockup { position: absolute; display: flex; align-items: center; gap: 7px; }
  .lockup .mark {
    border-radius: 50%;
    background: var(--brand-blue);
    flex: none;
  }
  .lockup .name {
    display: block;
    color: var(--brand-blue);
    font-weight: 400;
    line-height: 1;
  }
  .lockup .tagline {
    display: block;
    color: var(--ink-soft);
    line-height: 1.2;
  }
  .faint-mark {
    position: absolute;
    border-radius: 50%;
    background: radial-gradient(circle, var(--wash-orange) 0%, var(--wash-blue) 70%, transparent 72%);
  }

  /* business card back */
  .card-back { left: 29px; top: 365px; width: 144px; height: 84px; }
  .card-back .faint-mark { left: 42px; top: 12px; width: 60px; height: 60px; }
  .card-back .locations {
    position: absolute; left: 0; right: 0; top: 43px;
    text-align: center; font-size: 3.6px; color: var(--ink);
    letter-spacing: 0.05px;
  }

  /* business card front */
  .card-front { left: 29px; top: 461px; width: 144px; height: 86px; }
  .card-front .faint-mark { left: 70px; top: 8px; width: 70px; height: 70px; }
  .card-front .person { position: absolute; left: 40px; top: 10px; }
  .card-front .person-name { font-size: 4.6px; font-weight: 600; color: var(--brand-blue); }
  .card-front .person-role { font-size: 3.4px; color: var(--ink-soft); }
  .card-front .contact {
    position: absolute; left: 40px; top: 27px;
    font-size: 3.2px; line-height: 4.4px; color: var(--ink);
  }

  /* letterhead */
  .letterhead { left: 192px; top: 19px; width: 384px; height: 646px; }
  .letterhead .lockup { left: 145px; top: 16px; }
  .letterhead .mark { width: 22px; height: 22px; }
  .letterhead .name { font-size: 15px; }
  .letterhead .tagline { font-size: 4.6px; }
  .letterhead .faint-mark { left: 108px; top: 212px; width: 180px; height: 180px; }
  .letterhead .footer {
    position: absolute; left: 0; right: 0; top: 578px; text-align: center;
  }
  .letterhead .web { font-size: 6px; font-weight: 600; color: var(--ink); }
  .letterhead .address { font-size: 3.6px; color: var(--ink-soft); margin-top: 3px; }

  /* envelope back */
  .envelope-back { left: 631px; top: 72px; width: 550px; height: 264px; }
  .envelope-back svg { position: absolute; inset: 0; }
  .envelope-back .lockup { left: 270px; top: 108px; gap: 0; }
  .envelope-back .mark { width: 18px; height: 18px; }

  /* envelope front */
  .envelope-front { left: 631px; top: 360px; width: 550px; height: 259px; }
  .envelope-front .lockup { left: 234px; top: 52px; }
  .envelope-front .mark { width: 22px; height: 22px; }
  .envelope-front .name { font-size: 15px; }
  .envelope-front .tagline { font-size: 4.6px; }
  .envelope-front .footer {
    position: absolute; left: 0; right: 0; top: 180px; text-align: center;
  }
  .envelope-front .web { font-size: 6px; font-weight: 600; color: var(--ink); }
  .envelope-front .address { font-size: 3.6px; color: var(--ink-soft); margin-top: 3px; }
  .envelope-front .faint-mark { left: 245px; top: 200px; width: 60px; height: 60px; }
</style>
</head>
<body>

  <section class="sheet card-back" aria-label="Business card back">
    <div class="faint-mark" role="img" aria-label="Faint brand mark decoration"></div>
    <p class="locations">London | New York | Amsterdam | Munich | Silicon Valley</p>
  </section>

  <section class="sheet card-front" aria-label="Business card front">
    <div class="faint-mark" role="img" aria-label="Faint brand mark decoration"></div>
    <div class="person">
      <p class="person-name">Denise Okafor</p>
      <p class="person-role">Account Manager</p>
    </div>
    <div class="contact">
      <p>T: +44 (0) 1256 555 014</p>
      <p>F: +44 (0) 1256 555 015</p>
      <p>denise.okafor@helixmarke.co.uk</p>
      <p>Wexford Court, Brindle Road</p>
      <p>Chertsey, Surrey RG21 4XN UK</p>
      <p>www.helixmarke.co.uk</p>
    </div>
  </section>

  <section class="sheet letterhead" aria-label="Letterhead">
    <div class="lockup">
      <span class="mark"></span>
      <div>
        <span class="name">Helix Marke</span>
        <span class="tagline">Lead Generation Specialists</span>
      </div>
    </div>
    <div class="faint-mark" role="img" aria-label="Faint brand mark decoration"></div>
    <div class="footer">
      <p class="web">www.helixmarke.co.uk</p>
      <p class="address">E: denise.okafor@helixmarke.co.uk | A: Wexford Court, Brindle Road, Chertsey, Surrey RG21 4XN | T: +44 (0) 1256 555 014 | F: +44 (0) 1256 555 015</p>
    </div>
  </section>

  <section class="sheet envelope-back" aria-label="Envelope back">
    <svg width="550" height="264" viewBox="0 0 550 264" aria-hidden="true">
      <polyline points="0,0 275,122 550,0" fill="none" stroke="var(--fold)" stroke-width="1.2"/>
      <line x1="0" y1="264" x2="250" y2="150" stroke="var(--fold)" stroke-width="1"/>
      <line x1="550" y1="264" x2="300" y2="150" stroke="var(--fold)" stroke-width="1"/>
    </svg>
    <div class="lockup"><span class="mark"></span></div>
  </section>

  <section class="sheet envelope-front" aria-label="Envelope front">
    <div class="lockup">
      <span class="mark"></span>
      <div>
        <span class="name">Helix Marke</span>
        <span class="tagline">Lead Generation Specialists</span>
      </div>
    </div>
    <div class="footer">
      <p class="web">www.helixmarke.co.uk</p>
      <p class="address">E: denise.okafor@helixmarke.co.uk | A: Wexford Court, Brindle Road, Chertsey, Surrey RG21 4XN | T: +44 (0) 1256 555 014</p>
    </div>
    <div class="faint-mark" role="img" aria-label="Faint brand mark decoration"></div>
  </section>

</body>
</html>
```